Empower our Electric Journey on the Web

We need a new website that can promote our services. Our three services that we offer are:
- Management of e-mobility charging stations
- Management of energy purchases
- Leasing of E-Mobility charging stations
- Energy billing of private electricity meters
The website should work responsively on PC, tablet and smartphone. In general, a simple navigation and an appealing design should be in the foreground. The website should give the customer the possibility to request , based pm a preset chexkbox chart and to get in contact with us.
Our logo works on black and white background.
Our slogan is:
Empower Your Electric Journey with Velmor Mobility
The 4 Pages should be the following:
Main Page, with info about us, why choose us,
2nd; services; what we sell and what are our services
3rd; Contact us, request an offer
4th, References about costumers and Work we already did, in the future we would like to integrate a Blog Post in this section in stead of references.

Target Market(s)

Landlords, Homeowners, Homeowner Associations

Industry/Entity Type

EV Chargers / E-Mobility

Coding

Coded - Design and coding required

Number of Pages Required

4 page

Requirements
Nice to have
• Pop up to our mailchimp newsletter subscription

```html
<!DOCTYPE html>
<html lang="en">
<head>
<meta charset="utf-8">
<title>Velmor Mobility – Home and Newsletter Popup</title>
<link href="https://fonts.googleapis.com/css2?family=Michroma&family=DM+Sans:wght@400;500;600&display=swap" rel="stylesheet">
<style>
:root{
  --green:#4cc13a;
  --green-light:#7ddc4a;
  --green-dark:#2f9a2a;
  --ink:#1c1c1c;
  --hero:#232323;
  --card:#2d2d2d;
  --footer:#1f1f1f;
  --paper:#ffffff;
  --soft:#f5f5f5;
  --muted:#555555;
  --head:"Michroma",sans-serif;
  --body:"DM Sans",sans-serif;
}
*{box-sizing:border-box;margin:0;padding:0}
html,body{width:964px;height:1200px;overflow:hidden;background:#fff}
body{position:relative;font-family:var(--body);color:var(--ink)}
.screen{position:absolute;top:18px;width:807px;height:2072px;transform:scale(.5566);transform-origin:0 0;overflow:hidden;background:var(--paper)}
.screen--home{left:20px}
.screen--popup{left:495px}

/* hero */
.hero{position:absolute;left:0;top:0;width:807px;height:828px;background:var(--hero);color:#fff}
.hero__photo{position:absolute;inset:0 0 360px 0;background:
  radial-gradient(ellipse 260px 320px at 560px 200px,#6a6a6a 0%,#3b3b3b 55%,transparent 100%),
  radial-gradient(ellipse 260px 220px at 200px 300px,#4a4a4a 0%,#2a2a2a 70%,transparent 100%),
  linear-gradient(180deg,#3a3a3a 0%,#2a2a2a 70%,var(--hero) 100%)}
.nav{position:absolute;left:75px;top:17px;right:76px;height:28px;display:flex;align-items:center}
.brand{display:flex;align-items:center;gap:7px;font-family:var(--body);font-weight:600;color:var(--green);font-size:15px;letter-spacing:.5px}
.brand__dot{width:12px;height:12px;background:var(--green)}
.nav__links{display:flex;gap:19px;margin-left:auto;margin-right:25px;font-size:10.5px}
.btn{display:inline-block;background:var(--green);color:#fff;font-family:var(--body);font-weight:500;font-size:10.5px;padding:7px 16px;clip-path:polygon(6px 0,100% 0,100% calc(100% - 6px),calc(100% - 6px) 100%,0 100%,0 6px)}
.hero__copy{position:absolute;left:434px;width:300px;top:134px;text-align:center}
.hero__kicker{font-family:var(--head);font-size:14px;letter-spacing:.5px}
.hero__title{font-family:var(--head);font-size:21px;font-weight:400;margin-top:10px;white-space:nowrap}
.hero__text{font-size:10.5px;line-height:19px;margin-top:12px}
.hero__down{width:17px;height:17px;border:1px solid #fff;border-radius:50%;margin:18px auto 0;display:flex;align-items:center;justify-content:center}

.services__title{position:absolute;top:462px;width:100%;text-align:center;font-family:var(--head);font-size:24px;font-weight:400}
.services__arrow{position:absolute;top:645px}
.card{position:absolute;top:532px;width:202px;height:218px}
.card::before{content:"";position:absolute;left:6px;top:28px;right:-2px;bottom:-2px;border-right:1.5px solid var(--green);border-bottom:1.5px solid var(--green)}
.card__body{position:absolute;inset:0 6px 6px 0;background:var(--card);clip-path:polygon(0 0,calc(100% - 24px) 0,100% 24px,100% 100%,0 100%);text-align:center;padding-top:18px}
.card__icon{height:44px}
.card__name{font-family:var(--head);font-size:8.5px;line-height:19px;margin-top:12px;min-height:57px;display:flex;align-items:center;justify-content:center}
.card__text{font-size:8.5px;line-height:17.5px;margin-top:9px;padding:0 10px}

/* intro */
.intro{position:absolute;top:828px;left:0;width:807px;text-align:center}
.intro__mark{width:16px;height:16px;background:var(--green);margin:73px auto 0}
.intro__title{font-family:var(--head);font-size:23px;font-weight:400;line-height:38px;margin-top:22px}

/* about */
.about__title{position:absolute;left:75px;top:1172px;font-family:var(--head);font-size:24px;font-weight:400}
.about__text{position:absolute;left:75px;top:1232px;width:345px;font-size:10px;line-height:19px;color:#333}
.about__text p+p{margin-top:10px}
.about__btn{position:absolute;left:75px;top:1404px}
.about__frame{position:absolute;left:455px;top:1177px;width:263px;height:251px;border:1.5px solid var(--green)}
.about__photo{position:absolute;left:468px;top:1165px;width:264px;height:251px;background:
  radial-gradient(ellipse 90px 110px at 90px 150px,#c7c9c2 0%,#8b8d84 60%,transparent 100%),
  linear-gradient(135deg,#5a3c2a 0%,#6b4a34 40%,#4e5a3a 75%,#2d3a22 100%)}

/* testimonials */
.reviews__title{position:absolute;top:1506px;width:100%;text-align:center;font-family:var(--head);font-size:22px;font-weight:400}
.reviews__band{position:absolute;left:146px;top:1585px;width:42px;height:193px;background:linear-gradient(180deg,var(--green-light),var(--green-dark))}
.reviews__card{position:absolute;left:190px;top:1585px;width:487px;height:193px;background:var(--soft);box-shadow:0 2px 10px rgba(0,0,0,.08);padding:20px 27px}
.reviews__name{font-size:14px;font-weight:500}
.reviews__role{font-size:10.5px;margin-top:10px;color:#333}
.reviews__text{font-size:9.5px;line-height:19px;margin-top:11px;color:#333}
.reviews__text+.reviews__text{margin-top:6px}
.reviews__arrow{position:absolute;top:1672px}

/* footer */
.footer{position:absolute;left:0;top:1850px;width:807px;height:222px;background:var(--footer);color:#fff}
.footer .brand{position:absolute;left:75px;top:34px;font-size:21px;gap:10px}
.footer .brand__dot{width:16px;height:16px}
.footer__links{position:absolute;right:75px;top:38px;display:flex;gap:30px;font-size:10.5px}
.contact{position:absolute;top:112px;display:flex;gap:12px;font-size:10.5px;line-height:20px}
.footer__rule{position:absolute;left:75px;right:75px;top:178px;border-top:1px solid #555}
.footer__copy{position:absolute;left:75px;top:191px;font-size:10px}
.socials{position:absolute;right:75px;top:188px;display:flex;gap:7px}
.socials span{width:22px;height:22px;border:1px solid #fff;border-radius:50%}

/* popup */
.overlay{position:absolute;inset:0;background:rgba(0,0,0,.72)}
.modal{position:absolute;left:128px;top:171px;width:558px;height:285px;background:#fff;border:3px solid #9a9a9a;text-align:center}
.modal__close{position:absolute;right:18px;top:16px}
.modal__title{font-family:var(--head);font-size:24px;font-weight:400;line-height:38px;margin-top:20px}
.field{width:354px;height:40px;margin:12px auto 0;border:1px solid #e2e2e2;text-align:left;padding-left:18px;font-size:10.5px;line-height:38px;box-shadow:0 1px 4px rgba(0,0,0,.06)}
.modal .btn{margin-top:24px}
</style>
</head>
<body>

<!-- Home page -->
<section class="screen screen--home">
  <header class="hero">
    <div class="hero__photo" role="img" aria-label="Electric car plugged into a charging station in a dim garage"></div>
    <nav class="nav">
      <div class="brand"><span class="brand__dot"></span>VELMOR MOBILITY</div>
      <div class="nav__links"><span>Home</span><span>About</span><span>Services</span><span>Reviews</span><span>Blog</span><span>Contact</span></div>
      <span class="btn">Get Started</span>
    </nav>
    <div class="hero__copy">
      <p class="hero__kicker">WELCOME TO</p>
      <h1 class="hero__title">VELMOR MOBILITY</h1>
      <p class="hero__text">Lorem ipsum dolor sit amet, consectetur adipiscing elit, sed do eiusmod tempor incididunt ut labore et dolore.</p>
      <div class="hero__down"><svg width="9" height="9" viewBox="0 0 10 10"><path d="M5 1v8M2 6l3 3 3-3" stroke="#fff" fill="none"/></svg></div>
    </div>
    <h2 class="services__title">OUR SERVICES</h2>
    <svg class="services__arrow" style="left:30px" width="18" height="22" viewBox="0 0 18 22"><path d="M14 2 4 11l10 9" stroke="var(--green)" stroke-width="4" fill="none"/></svg>
    <svg class="services__arrow" style="left:760px" width="18" height="22" viewBox="0 0 18 22"><path d="M4 2l10 9-10 9" stroke="var(--green)" stroke-width="4" fill="none"/></svg>
    <article class="card" style="left:74px"><div class="card__body">
      <svg class="card__icon" width="36" viewBox="0 0 36 44" fill="none" stroke="#fff" stroke-width="1.5"><rect x="4" y="3" width="18" height="36" rx="2"/><rect x="8" y="7" width="10" height="7"/><path d="M14 18l-3 6h5l-3 6"/><path d="M2 40h22M22 12h6v20a3 3 0 0 0 6 0V8M31 3v5M35 3v5"/></svg>
      <h3 class="card__name">MANAGEMENT OF<br>E-MOBILITY CHARGING<br>STATIONS</h3>
      <p class="card__text">Lorem ipsum dolor sit amet, consectetur adipiscing elit, sed do eiusmod tempor incunt ut labore et dolore magna aliqua.</p>
    </div></article>
    <article class="card" style="left:303px"><div class="card__body">
      <svg class="card__icon" width="44" viewBox="0 0 44 44" fill="none" stroke="#fff" stroke-width="1.5"><circle cx="22" cy="22" r="11"/><path d="M22 3v6M22 35v6M3 22h6M35 22h6M8.5 8.5l4 4M31.5 31.5l4 4M8.5 35.5l4-4M31.5 12.5l4-4"/><path d="M24 15l-5 8h6l-5 8"/></svg>
      <h3 class="card__name">MANAGEMENT OF<br>ENERGY PURCHASES</h3>
      <p class="card__text">Lorem ipsum dolor sit amet, consectetur adipiscing elit, sed do eiusmod tempor incunt ut labore et dolore magna aliqua.</p>
    </div></article>
    <article class="card" style="left:531px"><div class="card__body">
      <svg class="card__icon" width="46" viewBox="0 0 46 44" fill="none" stroke="#fff" stroke-width="1.5"><path d="M12 14l4-7h14l4 7v6H12z"/><circle cx="18" cy="17" r="1.5"/><circle cx="28" cy="17" r="1.5"/><path d="M3 28l8-4 12 3h6a3 3 0 0 1 0 6H19M3 38l10-3 14 2 14-10"/></svg>
      <h3 class="card__name">LEASING OF<br>E-MOBILITY CHARGING<br>STATIONS</h3>
      <p class="card__text">Lorem ipsum dolor sit amet, consectetur adipiscing elit, sed do eiusmod tempor incunt ut labore et dolore magna aliqua.</p>
    </div></article>
  </header>

  <section class="intro">
    <div class="intro__mark"></div>
    <h2 class="intro__title">EMPOWER YOUR ELECTRIC<br>JOURNEY WITH VELMOR MOBILITY</h2>
  </section>

  <h2 class="about__title">ABOUT US</h2>
  <div class="about__text">
    <p>Lorem ipsum dolor sit amet, consectetur adipiscing elit, sed do eius mod tempor incididunt ut labore et dolore magna aliqua. Quis ipsum suspendisse ultrices gravida. Risus commodo viverra maecenas ac cumsan lacus vel facilisis.</p>
    <p>Sed do eius mod tempor incididunt ut labore et dolore magna aliqua. Quis ipsum suspendisse ultrices gravida. Risus commodo viverra mae cenas ac cumsan lacus vel facilisis.</p>
  </div>
  <span class="btn about__btn">Get Started</span>
  <div class="about__frame"></div>
  <div class="about__photo" role="img" aria-label="White electric car charging at a wall-side charger beside a house"></div>

  <h2 class="reviews__title">CLIENT TESTIMONIALS</h2>
  <svg class="reviews__arrow" style="left:76px" width="18" height="22" viewBox="0 0 18 22"><path d="M14 2 4 11l10 9" stroke="var(--green)" stroke-width="4" fill="none"/></svg>
  <svg class="reviews__arrow" style="left:714px" width="18" height="22" viewBox="0 0 18 22"><path d="M4 2l10 9-10 9" stroke="var(--green)" stroke-width="4" fill="none"/></svg>
  <div class="reviews__band" role="img" aria-label="Green decorative stripe"></div>
  <blockquote class="reviews__card">
    <p class="reviews__name">Owen Fairlie</p>
    <p class="reviews__role">Lorem ipsum dolor sit amet</p>
    <p class="reviews__text">Lorem ipsum dolor sit amet, consectetur adipiscing eli, sed do eiusmod tempor incididunt ut labore et dolmagna aliqua. Quis ipsum suspendisse ultrices gravi da. Risus commodo viverra maecenas accumsan lacus vel facilisis.</p>
    <p class="reviews__text">Eiusmod tempor incididunt ut labore et dolmagna aliqua. Quis ips suspendissultrices gravi da. Risus commodo viverra maecenas accumsan.</p>
  </blockquote>

  <footer class="footer">
    <div class="brand"><span class="brand__dot"></span>VELMOR MOBILITY</div>
    <div class="footer__links"><span>Home</span><span>About</span><span>Services</span><span>Reviews</span><span>Blog</span><span>Contact</span></div>
    <div class="contact" style="left:75px"><svg width="16" height="18" viewBox="0 0 16 18"><path d="M8 1a6 6 0 0 0-6 6c0 4 6 10 6 10s6-6 6-10a6 6 0 0 0-6-6z" fill="#fff"/><circle cx="8" cy="7" r="2.3" fill="var(--footer)"/></svg><p>Velmor mobility,<br>Address Comes Here</p></div>
    <div class="contact" style="left:325px"><svg width="17" height="17" viewBox="0 0 17 17"><path d="M3 1l3 1 1 4-2 1.5a10 10 0 0 0 4.5 4.5L11 10l4 1 1 3-2 2C7 16 1 10 1 3z" fill="#fff"/></svg><p>Phone:<br>+1 555 014 2290</p></div>
    <div class="contact" style="left:545px"><svg width="18" height="13" viewBox="0 0 18 13"><rect width="18" height="13" fill="#fff"/><path d="M1 1l8 6 8-6" stroke="var(--footer)" stroke-width="1.4" fill="none"/></svg><p>Mail:<br>hello@velmormobility.com</p></div>
    <div class="footer__rule"></div>
    <p class="footer__copy">2023 Velmor Mobility. All Rights Reserved.</p>
    <div class="socials"><span></span><span></span><span></span></div>
  </footer>
</section>

<!-- Home page with newsletter popup -->
<section class="screen screen--popup">
  <header class="hero">
    <div class="hero__photo" role="img" aria-label="Electric car plugged into a charging station in a dim garage"></div>
    <nav class="nav">
      <div class="brand"><span class="brand__dot"></span>VELMOR MOBILITY</div>
      <div class="nav__links"><span>Home</span><span>About</span><span>Services</span><span>Reviews</span><span>Blog</span><span>Contact</span></div>
      <span class="btn">Get Started</span>
    </nav>
    <div class="hero__copy">
      <p class="hero__kicker">WELCOME TO</p>
      <h1 class="hero__title">VELMOR MOBILITY</h1>
      <p class="hero__text">Lorem ipsum dolor sit amet, consectetur adipiscing elit, sed do eiusmod tempor incididunt ut labore et dolore.</p>
      <div class="hero__down"><svg width="9" height="9" viewBox="0 0 10 10"><path d="M5 1v8M2 6l3 3 3-3" stroke="#fff" fill="none"/></svg></div>
    </div>
    <h2 class="services__title">OUR SERVICES</h2>
    <svg class="services__arrow" style="left:30px" width="18" height="22" viewBox="0 0 18 22"><path d="M14 2 4 11l10 9" stroke="var(--green)" stroke-width="4" fill="none"/></svg>
    <svg class="services__arrow" style="left:760px" width="18" height="22" viewBox="0 0 18 22"><path d="M4 2l10 9-10 9" stroke="var(--green)" stroke-width="4" fill="none"/></svg>
    <article class="card" style="left:74px"><div class="card__body">
      <svg class="card__icon" width="36" viewBox="0 0 36 44" fill="none" stroke="#fff" stroke-width="1.5"><rect x="4" y="3" width="18" height="36" rx="2"/><rect x="8" y="7" width="10" height="7"/><path d="M14 18l-3 6h5l-3 6"/><path d="M2 40h22M22 12h6v20a3 3 0 0 0 6 0V8M31 3v5M35 3v5"/></svg>
      <h3 class="card__name">MANAGEMENT OF<br>E-MOBILITY CHARGING<br>STATIONS</h3>
      <p class="card__text">Lorem ipsum dolor sit amet, consectetur adipiscing elit, sed do eiusmod tempor incunt ut labore et dolore magna aliqua.</p>
    </div></article>
    <article class="card" style="left:303px"><div class="card__body">
      <svg class="card__icon" width="44" viewBox="0 0 44 44" fill="none" stroke="#fff" stroke-width="1.5"><circle cx="22" cy="22" r="11"/><path d="M22 3v6M22 35v6M3 22h6M35 22h6M8.5 8.5l4 4M31.5 31.5l4 4M8.5 35.5l4-4M31.5 12.5l4-4"/><path d="M24 15l-5 8h6l-5 8"/></svg>
      <h3 class="card__name">MANAGEMENT OF<br>ENERGY PURCHASES</h3>
      <p class="card__text">Lorem ipsum dolor sit amet, consectetur adipiscing elit, sed do eiusmod tempor incunt ut labore et dolore magna aliqua.</p>
    </div></article>
    <article class="card" style="left:531px"><div class="card__body">
      <svg class="card__icon" width="46" viewBox="0 0 46 44" fill="none" stroke="#fff" stroke-width="1.5"><path d="M12 14l4-7h14l4 7v6H12z"/><circle cx="18" cy="17" r="1.5"/><circle cx="28" cy="17" r="1.5"/><path d="M3 28l8-4 12 3h6a3 3 0 0 1 0 6H19M3 38l10-3 14 2 14-10"/></svg>
      <h3 class="card__name">LEASING OF<br>E-MOBILITY CHARGING<br>STATIONS</h3>
      <p class="card__text">Lorem ipsum dolor sit amet, consectetur adipiscing elit, sed do eiusmod tempor incunt ut labore et dolore magna aliqua.</p>
    </div></article>
  </header>

  <section class="intro">
    <div class="intro__mark"></div>
    <h2 class="intro__title">EMPOWER YOUR ELECTRIC<br>JOURNEY WITH VELMOR MOBILITY</h2>
  </section>

  <h2 class="about__title">ABOUT US</h2>
  <div class="about__text">
    <p>Lorem ipsum dolor sit amet, consectetur adipiscing elit, sed do eius mod tempor incididunt ut labore et dolore magna aliqua. Quis ipsum suspendisse ultrices gravida. Risus commodo viverra maecenas ac cumsan lacus vel facilisis.</p>
    <p>Sed do eius mod tempor incididunt ut labore et dolore magna aliqua. Quis ipsum suspendisse ultrices gravida. Risus commodo viverra mae cenas ac cumsan lacus vel facilisis.</p>
  </div>
  <span class="btn about__btn">Get Started</span>
  <div class="about__frame"></div>
  <div class="about__photo" role="img" aria-label="White electric car charging at a wall-side charger beside a house"></div>

  <h2 class="reviews__title">CLIENT TESTIMONIALS</h2>
  <svg class="reviews__arrow" style="left:76px" width="18" height="22" viewBox="0 0 18 22"><path d="M14 2 4 11l10 9" stroke="var(--green)" stroke-width="4" fill="none"/></svg>
  <svg class="reviews__arrow" style="left:714px" width="18" height="22" viewBox="0 0 18 22"><path d="M4 2l10 9-10 9" stroke="var(--green)" stroke-width="4" fill="none"/></svg>
  <div class="reviews__band" role="img" aria-label="Green decorative stripe"></div>
  <blockquote class="reviews__card">
    <p class="reviews__name">Owen Fairlie</p>
    <p class="reviews__role">Lorem ipsum dolor sit amet</p>
    <p class="reviews__text">Lorem ipsum dolor sit amet, consectetur adipiscing eli, sed do eiusmod tempor incididunt ut labore et dolmagna aliqua. Quis ipsum suspendisse ultrices gravi da. Risus commodo viverra maecenas accumsan lacus vel facilisis.</p>
    <p class="reviews__text">Eiusmod tempor incididunt ut labore et dolmagna aliqua. Quis ips suspendissultrices gravi da. Risus commodo viverra maecenas accumsan.</p>
  </blockquote>

  <footer class="footer">
    <div class="brand"><span class="brand__dot"></span>VELMOR MOBILITY</div>
    <div class="footer__links"><span>Home</span><span>About</span><span>Services</span><span>Reviews</span><span>Blog</span><span>Contact</span></div>
    <div class="contact" style="left:75px"><svg width="16" height="18" viewBox="0 0 16 18"><path d="M8 1a6 6 0 0 0-6 6c0 4 6 10 6 10s6-6 6-10a6 6 0 0 0-6-6z" fill="#fff"/><circle cx="8" cy="7" r="2.3" fill="var(--footer)"/></svg><p>Velmor mobility,<br>Address Comes Here</p></div>
    <div class="contact" style="left:325px"><svg width="17" height="17" viewBox="0 0 17 17"><path d="M3 1l3 1 1 4-2 1.5a10 10 0 0 0 4.5 4.5L11 10l4 1 1 3-2 2C7 16 1 10 1 3z" fill="#fff"/></svg><p>Phone:<br>+1 555 014 2290</p></div>
    <div class="contact" style="left:545px"><svg width="18" height="13" viewBox="0 0 18 13"><rect width="18" height="13" fill="#fff"/><path d="M1 1l8 6 8-6" stroke="var(--footer)" stroke-width="1.4" fill="none"/></svg><p>Mail:<br>hello@velmormobility.com</p></div>
    <div class="footer__rule"></div>
    <p class="footer__copy">2023 Velmor Mobility. All Rights Reserved.</p>
    <div class="socials"><span></span><span></span><span></span></div>
  </footer>

  <div class="overlay"></div>
  <div class="modal" role="dialog" aria-label="Newsletter subscription">
    <svg class="modal__close" width="20" height="20" viewBox="0 0 20 20" fill="none" stroke="#222" stroke-width="1.3"><circle cx="10" cy="10" r="9"/><path d="M6.5 6.5l7 7M13.5 6.5l-7 7"/></svg>
    <h2 class="modal__title">SUBSCRIBE TO OUR<br>NEWSLETTER</h2>
    <div class="field">Name</div>
    <div class="field">Email Address</div>
    <span class="btn">Get Started</span>
  </div>
</section>

</body>
</html>
```